Design Personal Trainer Business Cards

****FIINAL FILES MUST BE SUBMITTED AS PSD LAYERED FILES WITH EDITABLE TEXT (300dpi, CMYK color)****

Design business cards with a personal fitness trainer theme

Cards should be standard US size (2" X 3.5" with 1/8" bleed on each side)

Use the color scheme from the logo

The trainer's picture should be on at least one side of the card. If you put his picture on both sides, please use different pics (his pics attached as pic1, pic2 and pic3)

Use the info below for your mock ups:

Dane M.
RB-WLS, LOV
Founder and CEO

(802) 555-0148
bluehorizonfit@mailbox-sample.net
Facebook: BlueHorizonFit
Instagram: @bluehorizonfit
Twitter: @bhfstrong
Google: Blue Horizon Fit
Yelp: Blue Horizon Fit

(use icons for social media, dont spell out the word)

```html
<!DOCTYPE html>
<html lang="en">
<head>
<meta charset="UTF-8">
<title>Blue Horizon Fit – Business Cards</title>
<link href="https://fonts.googleapis.com/css2?family=Open+Sans:wght@400;600;700;800&display=swap" rel="stylesheet">
<style>
  :root {
    --stage: #22c6f3;
    --card-blush: #f8e6df;
    --card-white: #f8f7f6;
    --orange: #ec6a1e;
    --orange-light: #f58a3c;
    --orange-deep: #d9531a;
    --ink: #1d1d1d;
    --ink-soft: #3a3a3a;
    --photo-tone: #c9b7ad;
  }
  * { margin: 0; padding: 0; box-sizing: border-box; }
  html, body {
    width: 1200px; height: 933px; overflow: hidden;
    background: var(--stage);
    font-family: "Open Sans", Arial, sans-serif;
  }
  .canvas { position: relative; width: 1200px; height: 933px; }

  .card {
    position: absolute;
    border-radius: 18px;
    overflow: hidden;
    box-shadow: 7px 7px 5px rgba(0,0,0,0.55);
  }

  /* Front */
  .card-front {
    left: 240px; top: 27px; width: 704px; height: 402px;
    background: var(--card-blush);
  }
  .front-mark {
    position: absolute; left: 50%; top: 62px; transform: translateX(-50%);
    width: 150px; height: 150px; border-radius: 50%;
    background: var(--orange);
  }
  .front-name {
    position: absolute; left: 0; right: 0; top: 238px;
    text-align: center;
    font-weight: 800; font-size: 52px; line-height: 64px; letter-spacing: 1px;
    color: var(--orange);
  }
  .front-band { position: absolute; left: 0; bottom: 0; width: 704px; height: 50px; }
  .front-url {
    position: absolute; left: 0; right: 0; top: 358px;
    text-align: center; font-size: 17px; color: var(--ink-soft);
  }

  /* Back */
  .card-back {
    left: 244px; top: 463px; width: 700px; height: 417px;
    background: var(--card-blush);
  }
  .back-split { position: absolute; inset: 0; width: 700px; height: 417px; }
  .back-brand {
    position: absolute; left: 24px; top: 28px; width: 190px;
    display: flex; flex-direction: column; align-items: center; gap: 10px;
  }
  .back-brand-mark { width: 64px; height: 64px; border-radius: 50%; background: var(--orange); }
  .back-brand-name { font-weight: 800; font-size: 24px; line-height: 28px; color: var(--orange); white-space: nowrap; }

  .contact-list {
    position: absolute; left: 23px; top: 160px; list-style: none;
  }
  .contact-item {
    display: flex; align-items: center; height: 28.7px;
    font-size: 17px; color: var(--ink);
  }
  .contact-icon {
    width: 22px; height: 22px; margin-right: 14px; flex: none;
    border-radius: 4px; background: var(--orange);
    display: flex; align-items: center; justify-content: center;
  }
  .contact-icon svg { width: 15px; height: 15px; }
  .contact-tab {
    position: absolute; left: 23px; bottom: 0; width: 22px; height: 18px;
    border-radius: 8px 8px 0 0; background: var(--orange);
  }

  .trainer-photo {
    position: absolute; left: 433px; top: 33px; width: 234px; height: 234px;
    border-radius: 50%;
    background: radial-gradient(circle at 50% 45%, #e6ddd8 0%, var(--photo-tone) 60%, #5b4a42 100%);
    border: 3px solid #fff;
  }
  .trainer-name {
    position: absolute; left: 460px; width: 180px; top: 273px;
    text-align: center; font-weight: 600; font-size: 30px; line-height: 38px; color: var(--ink);
  }
  .trainer-rule {
    position: absolute; left: 476px; top: 313px; width: 149px; height: 2px; background: var(--orange);
  }
  .trainer-creds {
    position: absolute; left: 440px; width: 220px; top: 318px;
    text-align: center; font-size: 16px; line-height: 19px; color: var(--ink);
  }
</style>
</head>
<body>
<main class="canvas">

  <section class="card card-front" aria-label="Card front">
    <div class="front-mark"></div>
    <div class="front-name">Blue Horizon Fit</div>
    <svg class="front-band" viewBox="0 0 704 50" aria-hidden="true">
      <polygon points="0,8 260,30 444,30 704,8 704,50 0,50" fill="var(--orange)"/>
      <polygon points="0,22 220,40 484,40 704,22 704,50 0,50" fill="var(--orange-deep)"/>
      <polygon points="0,0 140,20 0,30" fill="var(--orange-light)"/>
      <polygon points="704,0 564,20 704,30" fill="var(--orange-light)"/>
      <polygon points="250,30 454,30 444,36 260,36" fill="var(--card-blush)"/>
    </svg>
    <div class="front-url">www.BlueHorizonFit.com</div>
  </section>

  <section class="card card-back" aria-label="Card back">
    <svg class="back-split" viewBox="0 0 700 417" aria-hidden="true">
      <polygon points="0,0 315,0 435,417 0,417" fill="var(--card-white)"/>
      <polygon points="313,0 327,0 447,417 433,417" fill="var(--orange)"/>
    </svg>

    <div class="back-brand">
      <span class="back-brand-mark"></span>
      <span class="back-brand-name">Blue Horizon Fit</span>
    </div>

    <ul class="contact-list">
      <li class="contact-item"><span class="contact-icon"><svg viewBox="0 0 16 16"><path d="M4 1.5l2.2 3-1.3 1.6c.8 1.8 2.2 3.2 4 4l1.6-1.3 3 2.2-1.2 2.4C7 13.5 2.5 9 2.1 2.7z" fill="#fff"/></svg></span>(802) 555-0148</li>
      <li class="contact-item"><span class="contact-icon"><svg viewBox="0 0 16 16"><rect x="1.5" y="3.5" width="13" height="9" fill="none" stroke="#fff" stroke-width="1.6"/><path d="M1.5 3.5L8 9l6.5-5.5" fill="none" stroke="#fff" stroke-width="1.6"/></svg></span>bluehorizonfit@mailbox-sample.net</li>
      <li class="contact-item"><span class="contact-icon"><svg viewBox="0 0 16 16"><circle cx="8" cy="8" r="6.2" fill="none" stroke="#fff" stroke-width="1.4"/><ellipse cx="8" cy="8" rx="2.6" ry="6.2" fill="none" stroke="#fff" stroke-width="1.2"/><path d="M1.8 8h12.4" stroke="#fff" stroke-width="1.2"/></svg></span>BlueHorizonFit.com</li>
      <li class="contact-item"><span class="contact-icon"></span>BlueHorizonFit</li>
      <li class="contact-item"><span class="contact-icon"></span>@bluehorizonfit</li>
      <li class="contact-item"><span class="contact-icon"></span>@bhfstrong</li>
      <li class="contact-item"><span class="contact-icon"></span>Blue Horizon Fit</li>
      <li class="contact-item"><span class="contact-icon"></span>Blue Horizon Fit</li>
    </ul>
    <div class="contact-tab"></div>

    <div class="trainer-photo" role="img" aria-label="Portrait photo of the trainer, arms crossed, wearing a black branded t-shirt"></div>
    <div class="trainer-name">Dane M.</div>
    <div class="trainer-rule"></div>
    <div class="trainer-creds">RB-WLS, LOV<br>Founder and CEO</div>
  </section>

</main>
</body>
</html>
```